Oil Field Service company needs professional business cards

Looking to clean up our current company business cards and look a little more professional. Harlow Casing Services is a US based company that services the oil field. We deal with engineers, managers and oil rigs....................................................................................................................................................................................................................................................................................................................................................................................................

Target Market(s)

Oil and Gas professionals

Industry/Entity Type

Oil And Gas

Contact Information for Business Card

See attached photo as example

Font styles to use
Sans Serif

Colors
ec1f27

Requirements
Must have
• Company Logo, Name, Title, Cell, Office, Fax, Email.
• See attached photo
Nice to have
• External CRT, Internal CRT, Casing Crews, Torque Turn, Laydown Machine
Should not have
• Do not introduce any new pictures and keep it professional looking

```html
<!DOCTYPE html>
<html lang="en">
<head>
<meta charset="utf-8">
<title>Harlow Casing Services – Business Card</title>
<link rel="stylesheet" href="https://fonts.googleapis.com/css2?family=Montserrat:wght@400;600;700&family=Open+Sans:wght@400;600&family=Merriweather:wght@400&display=swap">
<style>
  :root{
    --bg:#dcdbdc;
    --card-dark:#1f1f1f;
    --card-light:#f3f3f3;
    --slate:#3e4b55;
    --slate-dim:#46525b;
    --red:#ec1f27;
    --ink:#1a1a1a;
    --muted:#333;
  }
  *{box-sizing:border-box;margin:0;padding:0}
  html,body{width:1200px;height:900px;overflow:hidden;background:var(--bg)}
  body{position:relative;font-family:"Open Sans",sans-serif}
  .card{
    position:absolute;left:290px;width:620px;height:354px;border-radius:26px;
    box-shadow:0 6px 18px rgba(0,0,0,.18);overflow:hidden;
  }
  .card--back{top:62px;background:var(--card-dark)}
  .card--front{top:484px;background:linear-gradient(100deg,#ffffff 0%,var(--card-light) 60%,#e9e9e9 100%)}

  .brand{position:absolute;display:flex;align-items:center;gap:14px}
  .brand__dot{width:20px;height:20px;border-radius:50%;background:var(--red);flex:none}
  .brand__name{font-family:"Montserrat",sans-serif;font-weight:700;color:var(--slate);letter-spacing:.5px;line-height:1.1}

  .card--back .brand{left:0;right:0;top:118px;justify-content:center}
  .card--back .brand__name{font-size:38px;color:var(--slate-dim)}
  .services{
    position:absolute;left:0;right:0;bottom:46px;text-align:center;
    font-family:"Montserrat",sans-serif;font-size:15px;color:#3a3f44;letter-spacing:.3px;
  }
  .services span{margin:0 10px}

  .card--front .brand{left:38px;top:150px;width:290px;flex-wrap:nowrap}
  .card--front .brand__name{font-size:27px}

  .divider{position:absolute;left:338px;top:62px;width:2px;height:230px;background:var(--ink)}
  .contact{position:absolute;left:366px;top:58px}
  .contact__name{font-family:"Montserrat",sans-serif;font-size:25px;color:var(--ink);font-weight:400}
  .contact__name strong{font-weight:700}
  .contact__title{font-family:"Merriweather",serif;font-size:15px;color:var(--red);margin-top:2px;margin-left:22px}
  .contact__list{list-style:none;margin-top:26px;margin-left:46px}
  .contact__list li{display:flex;align-items:center;gap:12px;font-size:15px;color:var(--muted);height:27px}
  .contact__list svg{width:15px;height:15px;flex:none;fill:var(--red)}
</style>
</head>
<body>

<section class="card card--back" aria-label="Card back">
  <div class="brand"><span class="brand__dot"></span><span class="brand__name">Harlow Casing Services</span></div>
  <p class="services">Laydon Machine<span>|</span>Casing Crew<span>|</span>Murd Tool<span>|</span>Torque Turn</p>
</section>

<section class="card card--front" aria-label="Card front">
  <div class="brand"><span class="brand__dot"></span><span class="brand__name">Harlow Casing Services</span></div>
  <div class="divider"></div>
  <div class="contact">
    <p class="contact__name">Casey <strong>Brennan</strong></p>
    <p class="contact__title">Area Manager</p>
    <ul class="contact__list">
      <li><svg viewBox="0 0 16 16"><path d="M1 6c0-2 3-4 7-4s7 2 7 4v1h-4V5.5H5V7H1zM3 8h10l2 6H1z"/></svg>555 210-4400</li>
      <li><svg viewBox="0 0 16 16"><path d="M4 1h8v14H4zM5.5 2.5v9h5v-9z"/></svg>555 318-2275</li>
      <li><svg viewBox="0 0 16 16"><path d="M4 1h8v5H4zM1 7h14v6h-2v2H3v-2H1zM5 11v3h6v-3z"/></svg>555 210-4415</li>
      <li><svg viewBox="0 0 16 16"><path d="M8 1a5 5 0 0 1 5 5c0 4-5 9-5 9S3 10 3 6a5 5 0 0 1 5-5zm0 3a2 2 0 1 0 0 4 2 2 0 0 0 0-4z"/></svg>Ridgeview, OK 73990</li>
      <li><svg viewBox="0 0 16 16"><path d="M1 3h14v1L8 9 1 4zM1 6l7 5 7-5v7H1z"/></svg>cbrennan@example.com</li>
    </ul>
  </div>
</section>

</body>
</html>
```